Banner, Backwall and Desk Wrap - Design

Must have by Monday 12th 8am Sydney Time.
We need two Banner designs to meet attached specs.
We need one wall design to meet attached specs.
We need one desk wrap design to meet attached specs.

The wall banner can be based off the two separate banners - am open to ideas on this

We are a Cloud telephony and internet provider. Our Websites are
www.brindlevox.com.au
www.tallyport.com.au
Banners will be created under the Brindlevox brand

I have included a word document with some ideas - but please be creative as I'm not a designer.

Theme must carry across all banners as they are for trade shows

I have also included the following - sample cloud backgrounds (you do not have to use them - if you have a better idea) - a sample business card we use - Two sample logos - square and horizontal.
A Desk Perks logo - unfortunately I do not have this graphic in high quality so it will have to be redesigned. It doesn't have to match
Desktop Wrap will be logo and background

Notes from Questions Asked
1) The deskwrap spcs are in the file called Graphic Wall Skirt
2) There will be Two separate Banners with Content from Word Doc. One will be based around VoIP and the other around Internet. Background Wall can be a combination of the banners laid out in a professional manner.

Apologies to all: The Printyard has now supplied me the correct measurements in PDFs these have now been uploaded

Target Market(s)

Small to Medium Business Market

Requirements
Must have
• Must have designs for decision on Monday 8am Sydney Time to meet trade show
Nice to have
• Want Both Banner to be similar in design. Carry banner designs across to the back wall

```html
<!DOCTYPE html>
<html lang="en">
<head>
<meta charset="utf-8">
<title>Brindlevox Trade Show Set</title>
<link rel="stylesheet" href="https://fonts.googleapis.com/css2?family=Open+Sans:wght@600;700;800&display=swap">
<style>
  :root {
    --sky-top: #2f86ea;
    --sky-mid: #3a9cf0;
    --sky-low: #5fd0f7;
    --cloud: #5ad4f4;
    --ink-dark: #2f3b40;
    --white: #ffffff;
    --mint: #4ef0cf;
    --red: #c8283c;
    --orange: #d9663a;
    --amber: #c98a2c;
    --olive: #a9b12c;
    --lime: #86c92a;
    --blue-core: #3d8ff0;
  }
  * { margin: 0; padding: 0; box-sizing: border-box; }
  html, body { width: 1062px; height: 1200px; overflow: hidden; background: var(--white); }
  body { font-family: "Open Sans", Arial, sans-serif; color: var(--white); position: relative; }
  .canvas { position: relative; width: 1062px; height: 1200px; border: 1px solid #222; }
  .sky {
    position: absolute;
    background: linear-gradient(180deg, var(--sky-top) 0%, var(--sky-mid) 55%, var(--sky-low) 100%);
    overflow: hidden;
  }
  .centered { position: absolute; left: 0; right: 0; text-align: center; }
  .mark { position: absolute; left: 50%; transform: translateX(-50%); border-radius: 50%; background: var(--cloud); }
  .brand-name { font-weight: 800; color: var(--ink-dark); letter-spacing: 1px; }
  .services { font-weight: 800; color: var(--ink-dark); letter-spacing: 1px; }
  .tagline { font-weight: 700; line-height: 1.22; }
  .shadowed { text-shadow: 0 1px 3px rgba(0,0,40,.45); }

  .backwall { left: 76px; top: 18px; width: 909px; height: 572px; border-top: 1px solid #e33; border-bottom: 1px solid #e33; }
  .deskwrap { left: 49px; top: 678px; width: 465px; height: 206px; }
  .banner { top: 630px; width: 216px; height: 540px; }
  .banner-internet { left: 543px; }
  .banner-pbx { left: 801px; }

  .banner .subline { font-size: 11.5px; font-weight: 600; color: var(--ink-dark); }
  .banner .phone { font-size: 20px; font-weight: 700; }
  .banner .digits { font-size: 10px; font-weight: 700; letter-spacing: 4px; }
  .benefits { position: absolute; left: 34px; right: 4px; list-style: none; font-size: 13px; font-weight: 700; line-height: 1.1; }
  .benefits li { margin-bottom: 5px; padding-left: 8px; position: relative; }
  .benefits li::before { content: "\2022"; position: absolute; left: 0; }
  .banner-pbx .benefits { left: 26px; }
  .diagram { position: absolute; left: 0; top: 270px; width: 216px; height: 150px; }
  .save-now { font-size: 11px; font-weight: 700; position: absolute; left: 30px; }
  .offer { font-size: 21px; font-weight: 800; letter-spacing: .5px; }
  .banner .tagline { font-size: 12px; }
</style>
</head>
<body>
<div class="canvas">

  <section class="sky backwall" aria-label="Back wall">
    <div class="mark" style="top:50px;width:150px;height:150px;"></div>
    <div class="centered brand-name" style="top:198px;font-size:58px;">Brindlevox</div>
    <div class="centered services" style="top:274px;font-size:13px;">PHONES - DATA - INTERNET</div>
    <div class="centered tagline" style="top:310px;font-size:21px;">Helping Business Communicate<br>for over 25 Years</div>
  </section>

  <section class="sky deskwrap" aria-label="Desk wrap">
    <div class="mark" style="top:22px;width:76px;height:76px;"></div>
    <div class="centered brand-name" style="top:100px;font-size:30px;">Brindlevox</div>
    <div class="centered services" style="top:152px;font-size:7.5px;">PHONES - DATA - INTERNET</div>
    <div class="centered tagline" style="top:171px;font-size:9px;">Helping Business Communicate<br>for over 25 Years</div>
  </section>

  <section class="sky banner banner-internet" aria-label="Internet banner">
    <div class="mark" style="top:26px;width:72px;height:72px;"></div>
    <div class="centered brand-name" style="top:100px;font-size:28px;">Brindlevox</div>
    <div class="centered subline" style="top:150px;">Internet | Fibre | NBN | VoIP</div>
    <div class="centered phone shadowed" style="top:168px;">1300 TALK NOW</div>
    <div class="centered digits" style="top:193px;">( 825566 )</div>
    <ul class="benefits shadowed" style="top:214px;">
      <li>Internet to Suit You</li>
      <li>Carrier Grade SLA’s</li>
      <li>No Nonsense Support</li>
    </ul>
    <svg class="diagram" viewBox="0 270 216 150" font-family="Open Sans, Arial, sans-serif" font-weight="700" text-anchor="middle" fill="#fff">
      <g fill="#e8f0ff" opacity=".9">
        <path d="M107 316 l-4 5 h8 z"/><path d="M107 369 l-4 -5 h8 z"/>
        <path d="M134 329 l-6 1 l4 5 z"/><path d="M134 356 l-6 -1 l4 -5 z"/>
        <path d="M80 329 l6 1 l-4 5 z"/><path d="M80 356 l6 -1 l-4 -5 z"/>
      </g>
      <circle cx="107" cy="295" r="19" fill="var(--red)"/><text x="107" y="299" font-size="9">NBN</text>
      <circle cx="159" cy="318" r="20" fill="var(--orange)"/><text x="159" y="316" font-size="5.5">Multisite</text><text x="159" y="323" font-size="5.5">Connectivity</text>
      <circle cx="162" cy="370" r="20" fill="var(--amber)"/><text x="162" y="368" font-size="6">Metro</text><text x="162" y="375" font-size="6">Ethernet</text>
      <circle cx="107" cy="398" r="21" fill="var(--olive)"/><text x="107" y="396" font-size="6">Fibre</text><text x="107" y="403" font-size="6">Connections</text>
      <circle cx="52" cy="369" r="21" fill="var(--lime)"/><text x="52" y="372" font-size="8">VoIP</text>
      <circle cx="55" cy="318" r="19" fill="var(--lime)"/><text x="55" y="316" font-size="6">Multi</text><text x="55" y="323" font-size="6">Vendor</text>
      <circle cx="107" cy="342" r="22" fill="var(--blue-core)" stroke="#bfe3ff" stroke-width="1"/><text x="107" y="346" font-size="9.5">Internet</text>
    </svg>
    <div class="save-now shadowed" style="top:437px;">Save Now!</div>
    <div class="centered offer shadowed" style="top:446px;">FREE ANALYSIS</div>
    <div class="centered tagline shadowed" style="top:482px;">Helping Business Communicate<br>for over 25 Years</div>
  </section>

  <section class="sky banner banner-pbx" aria-label="Hosted PBX banner">
    <div class="mark" style="top:26px;width:72px;height:72px;"></div>
    <div class="centered brand-name" style="top:100px;font-size:28px;">Brindlevox</div>
    <div class="centered subline" style="top:150px;">Internet | Cloud | Voice</div>
    <div class="centered phone shadowed" style="top:168px;">1300 TALK NOW</div>
    <div class="centered digits" style="top:193px;">( 825566 )</div>
    <ul class="benefits shadowed" style="top:208px;">
      <li>Reduce your Telephone Costs Instantly</li>
      <li>Transition to VoIP</li>
      <li>Full Featured Hosted PBX</li>
    </ul>
    <svg class="diagram" viewBox="0 270 216 150" font-family="Open Sans, Arial, sans-serif" font-weight="700" text-anchor="middle" fill="#fff">
      <g fill="#e8f0ff" opacity=".9">
        <path d="M108 326 l-4 5 h8 z"/><path d="M108 380 l-4 -5 h8 z"/>
        <path d="M135 339 l-6 1 l4 5 z"/><path d="M135 367 l-6 -1 l4 -5 z"/>
        <path d="M81 339 l6 1 l-4 5 z"/><path d="M81 367 l6 -1 l-4 -5 z"/>
      </g>
      <circle cx="108" cy="304" r="18" fill="var(--red)"/><text x="108" y="302" font-size="5">IVR and Call</text><text x="108" y="308" font-size="5">Recording</text>
      <circle cx="159" cy="329" r="19" fill="var(--orange)"/><text x="159" y="331" font-size="5.5">Fax to Email</text>
      <circle cx="163" cy="379" r="20" fill="var(--amber)"/><text x="163" y="377" font-size="6">Mobile</text><text x="163" y="384" font-size="6">Phones</text>
      <circle cx="108" cy="403" r="22" fill="var(--olive)"/><text x="108" y="401" font-size="6">Remote</text><text x="108" y="408" font-size="6">Home Office</text>
      <circle cx="54" cy="377" r="19" fill="var(--lime)"/><text x="54" y="375" font-size="5">Office</text><text x="54" y="381" font-size="5">Phones</text>
      <circle cx="56" cy="329" r="20" fill="var(--lime)"/><text x="56" y="327" font-size="5">Remote</text><text x="56" y="333" font-size="5">Branch PBX</text>
      <circle cx="108" cy="353" r="22" fill="var(--blue-core)" stroke="#bfe3ff" stroke-width="1"/><text x="108" y="358" font-size="13">PBX</text>
    </svg>
    <div class="centered offer shadowed" style="top:446px;">FREE ANALYSIS</div>
    <div class="centered tagline shadowed" style="top:481px;">Helping Business Communicate<br>for over 25 Years</div>
  </section>

</div>
</body>
</html>
```